Leafline Nutrition

we provide nutritional consulting for loss weight and changing food habits. The clinic is promoting the life healthy, as well as natural and balanced diets that help in the control weight and for the treatment to diseases.

Reason: Waiting some desings.

Reason: Waiting some designers

Reason: Waiting for changes.

Target Market(s)

Mostly women and men aged 30-55, both with overweight, obesity and problems with your food habits.

Industry/Entity Type

Weight

Font styles to use
Script

Colors
cadf82
ffc214
b868aa
f68d4d
0393ce
33b7a4
acd037
cbdf83
eaf2cf

Requirements
Must have
• lively and natural colors
logo that evokes healthy weight, concept of healthy natural food
Nice to have
• Slim fit image with a elegant and simple design
Should not have
• Preferably not used photograps, old-Style, Boring colors

```html
<!DOCTYPE html>
<html lang="en">
<head>
<meta charset="utf-8">
<title>Leafline Nutrition – Business Cards</title>
<link href="https://fonts.googleapis.com/css2?family=Exo+2:wght@400;500;600&display=swap" rel="stylesheet">
<style>
  :root{
    --stage:#e6e7e8;
    --paper:#ffffff;
    --blue:#1492d4;
    --cyan:#21b0e0;
    --gold:#e3a915;
    --gold-light:#f6d13c;
    --orange:#f26a22;
    --ink:#2b3440;
    --brand:#1a86c8;
    --pill:rgba(255,255,255,0.16);
    --pill-line:rgba(255,255,255,0.55);
  }
  *{box-sizing:border-box;margin:0;padding:0}
  html,body{width:1200px;height:1200px;overflow:hidden}
  body{background:var(--stage);font-family:"Exo 2",sans-serif;position:relative}

  .card{position:absolute;top:200px;width:440px;height:780px;background:var(--paper);
        box-shadow:0 14px 30px rgba(0,0,0,.18);overflow:hidden;display:flex;flex-direction:column}
  .card--back{left:120px}
  .card--front{left:640px}

  .brand{display:flex;align-items:center;justify-content:center;gap:12px}
  .brand__dot{width:22px;height:22px;border-radius:50%;background:var(--cyan);flex:none}
  .brand__name{font-size:30px;font-weight:500;color:var(--brand);letter-spacing:.5px;white-space:nowrap}

  .card__head{background:var(--paper);display:flex;align-items:center;justify-content:center}
  .card--back .card__head{height:330px}
  .card--front .card__head{height:220px;padding-top:30px}

  .band{display:flex;align-items:center;padding:0 38px}
  .band--blue{background:var(--blue)}
  .band--cyan{background:var(--cyan)}
  .card--back .band{height:150px}

  .pill{display:flex;align-items:center;gap:16px;width:100%;height:56px;padding:0 14px;
        border-radius:6px;background:var(--pill);color:#fff;font-size:20px;letter-spacing:.3px;white-space:nowrap}
  .pill__icon{width:36px;height:36px;border:2px solid var(--pill-line);border-radius:5px;
        display:flex;align-items:center;justify-content:center;flex:none}
  .pill__icon svg{width:20px;height:20px;fill:none;stroke:#fff;stroke-width:2;stroke-linecap:round;stroke-linejoin:round}
  .pill__square{width:16px;height:16px;background:#fff;border-radius:2px}
  .pill--tall{height:84px;line-height:1.3;font-size:18px}

  .contact-gold{flex:1;padding:28px 38px 30px;display:flex;flex-direction:column;gap:20px;
        background:radial-gradient(ellipse at 50% 65%,var(--gold-light) 0%,var(--gold) 75%)}
  .person{margin-bottom:6px}
  .person__name{font-size:26px;font-weight:600;color:var(--orange);letter-spacing:1px;text-transform:uppercase}
  .person__role{font-size:18px;font-weight:500;color:var(--ink);letter-spacing:1px;text-transform:uppercase}
  .contact-gold .pill{background:rgba(255,255,255,.18)}
  .contact-blue{height:230px;background:var(--blue);padding:30px 38px;display:flex;flex-direction:column;gap:20px}
</style>
</head>
<body>

<section class="card card--back" aria-label="Card back">
  <div class="card__head">
    <div class="brand"><span class="brand__dot"></span><span class="brand__name">Leafline Nutrition</span></div>
  </div>
  <div class="band band--blue">
    <div class="pill"><span class="pill__icon"><span class="pill__square"></span></span>social.example/leafline</div>
  </div>
  <div class="band band--cyan">
    <div class="pill"><span class="pill__icon"><span class="pill__square"></span></span>posts.example/leafline</div>
  </div>
  <div class="band band--blue">
    <div class="pill"><span class="pill__icon"><span class="pill__square"></span></span>network.example/leafline</div>
  </div>
</section>

<section class="card card--front" aria-label="Card front">
  <div class="card__head">
    <div class="brand"><span class="brand__dot"></span><span class="brand__name">Leafline Nutrition</span></div>
  </div>
  <div class="contact-gold">
    <div class="person">
      <p class="person__name">Daniel Reyes</p>
      <p class="person__role">General Manager</p>
    </div>
    <div class="pill">
      <span class="pill__icon"><svg viewBox="0 0 24 24"><path d="M5 3h4l2 5-2.5 1.5a11 11 0 0 0 6 6L16 13l5 2v4a2 2 0 0 1-2 2A16 16 0 0 1 3 5a2 2 0 0 1 2-2z"/></svg></span>
      010 555 0147
    </div>
    <div class="pill">
      <span class="pill__icon"><svg viewBox="0 0 24 24"><rect x="3" y="5" width="18" height="14" rx="2"/><path d="M3 7l9 6 9-6"/></svg></span>
      hello@leafline.com
    </div>
  </div>
  <div class="contact-blue">
    <div class="pill">
      <span class="pill__icon"><svg viewBox="0 0 24 24"><circle cx="12" cy="12" r="9"/><path d="M3 12h18M12 3a14 14 0 0 1 0 18M12 3a14 14 0 0 0 0 18"/></svg></span>
      www.leaflinenutrition.com
    </div>
    <div class="pill pill--tall">
      <span class="pill__icon"><svg viewBox="0 0 24 24"><path d="M12 21s-7-7-7-12a7 7 0 0 1 14 0c0 5-7 12-7 12z"/><circle cx="12" cy="9" r="2.5"/></svg></span>
      <span>42 Orchard Lane, Unit 7<br>Greenfield East</span>
    </div>
  </div>
</section>

</body>
</html>
```